Webbanner-Design für Ebook - Unterwegs im Süden Ungarns ( Affiliate und Promivo)
Zielgruppe
Wir verkaufen Ebooks. In diesem Fall möchten wir Kroatien Liebhaber aufmerksam machen, dass es mittlerweile ein Buch gibt, welches all die Sehenswürdigkeiten und Routen bis nach Kroatien ausführlich beschreibt.
Aufgabenstellung
Da wir unseren Affiliate Partner die Möglichkeit geben wollen, unsere Produkte zu verkaufen, benötigen wir diesbezüglich gute Anzeigen mit verschiedener Größen. ( affiliate und Promivo )
Sollten Vorlagen / Stockfotos verwendet werden, dann bitte über bildfang
Ich habe einige Fotos welches wir bereits erworben haben hier hochgeladen.
Auch das Coverbild ist im Anhang.
Ideal wäre eine Buch-Abbildung für die Anzeigen.
3 Anzeigegrößen erforderlich
728 x 90 300 x 250 300 x 600

```html
<!DOCTYPE html>
<html lang="de">
<head>
<meta charset="utf-8">
<title>Unterwegs im Süden Ungarns – Werbebanner</title>
<link href="https://fonts.googleapis.com/css2?family=Oswald:wght@500;700&display=swap" rel="stylesheet">
<style>
:root{
  --red:#c8141b;
  --navy:#3b5685;
  --white:#ffffff;
  --sky:#b9d6ee;
  --sea:#2a78b8;
  --deep:#1b4f86;
  --green:#3f6b2c;
  --cover:#4a6fa3;
  --cover-edge:#2d4c7a;
}
*{box-sizing:border-box;margin:0;padding:0}
html,body{width:1195px;height:1200px;overflow:hidden;background:#fff}
body{position:relative;font-family:"Oswald",sans-serif;color:var(--white)}
.banner{position:absolute;overflow:hidden}
.photo{position:absolute;inset:0}
.photo-square{background:linear-gradient(180deg,var(--sky) 0%,#8fbfe2 18%,var(--sea) 32%,var(--green) 48%,#5b8a3c 58%,var(--sea) 70%,var(--deep) 100%)}
.photo-tall{background:linear-gradient(180deg,var(--sky) 0%,#9cc6e6 14%,var(--sea) 30%,#3c7a3a 42%,var(--green) 55%,var(--sea) 66%,var(--deep) 100%)}
.photo-wide{background:linear-gradient(90deg,var(--green) 0%,var(--sea) 14%,#7fb3dc 30%,#a9cde9 60%,var(--sea) 100%)}
.shout{position:absolute;text-transform:uppercase;font-weight:700;line-height:.9;text-shadow:0 2px 4px rgba(0,0,0,.55)}
.shout .line{display:block}
.shout .mid{font-size:.55em}
.tab-red{position:absolute;background:var(--red);font-weight:500;text-align:center;line-height:1.25;text-shadow:0 1px 2px rgba(0,0,0,.4)}
.tab-ebook{position:absolute;background:var(--navy);border-radius:10px 0 0 10px;font-weight:700;display:flex;align-items:center;justify-content:center;text-shadow:0 1px 2px rgba(0,0,0,.5)}
.topics{position:absolute;font-weight:700;line-height:1.18;text-shadow:0 2px 3px rgba(0,0,0,.6);list-style:none;white-space:nowrap}
.topics li::before{content:"• "}
.topics .lead::before{content:""}
.book{position:absolute;background:var(--cover);box-shadow:6px 8px 12px rgba(0,0,0,.45);border-left:4px solid var(--cover-edge);overflow:hidden}
.book-title{position:absolute;left:8%;top:4%;right:4%;font-weight:700;text-transform:uppercase;line-height:.9}
.book-sub{display:block;width:58%;font-weight:500;text-transform:none;line-height:1.1;margin-top:4%}
.book-art{position:absolute;left:0;right:0;top:48%;bottom:10%;background:linear-gradient(180deg,#d9a878 0%,#b97e54 40%,#7da0b8 60%,#5b7f48 100%)}
.book-author{position:absolute;left:0;right:0;bottom:2%;text-align:center;font-weight:500}
.book-seal{position:absolute;right:3%;top:40%;border-radius:50%;background:var(--red);border:2px solid var(--white);z-index:1}
.ad-square{left:101px;top:299px;width:467px;height:386px}
.ad-tall{left:605px;top:26px;width:467px;height:934px}
.ad-wide{left:22px;top:1022px;width:1133px;height:142px}
</style>
</head>
<body>

<section class="banner ad-square" aria-label="Banner 300 x 250">
  <div class="photo photo-square" role="img" aria-label="Luftbild einer Insel mit Meer und grünen Hügeln"></div>
  <div class="tab-red" style="left:251px;top:2px;width:216px;height:53px;font-size:18px;padding-top:3px">Der perfekte Guide<br>für Fahrer &amp; Beifahrer</div>
  <h2 class="shout" style="left:19px;top:20px;font-size:58px">
    <span class="line" style="font-size:26px">Unterwegs</span>
    <span class="line">Im <span class="mid">Süden</span></span>
    <span class="line">Ungarns</span>
  </h2>
  <div class="tab-ebook" style="left:17px;top:160px;width:124px;height:40px;font-size:24px">e-book</div>
  <ul class="topics" style="left:17px;top:226px;font-size:22px">
    <li class="lead">Alles über</li><li>Mautgebühren</li><li>Tunnelgebühren</li><li>Campingplätze</li><li>Sehenswürdigkeiten</li>
  </ul>
  <div class="book" style="left:272px;top:72px;width:160px;height:236px">
    <div class="book-title" style="font-size:25px">Unterwegs<br>im Süden<br>Ungarns<span class="book-sub" style="font-size:10px">Der perfekte Guide für Fahrer &amp; Beifahrer</span></div>
    <div class="book-seal" style="width:36px;height:36px"></div>
    <div class="book-art" role="img" aria-label="Coverfoto einer Altstadt am Meer"></div>
    <div class="book-author" style="font-size:10px">Lena Vostrik</div>
  </div>
</section>

<section class="banner ad-tall" aria-label="Banner 300 x 600">
  <div class="photo photo-tall" role="img" aria-label="Luftbild von Inseln im tiefblauen Meer"></div>
  <div class="tab-red" style="left:0;top:0;width:467px;height:140px;font-size:36px;padding-top:18px">Der perfekte Guide<br>für Fahrer &amp; Beifahrer</div>
  <h2 class="shout" style="left:50px;top:182px;font-size:84px">
    <span class="line" style="font-size:36px">Unterwegs</span>
    <span class="line">Im <span class="mid">Süden</span></span>
    <span class="line">Ungarns</span>
  </h2>
  <div class="tab-ebook" style="left:244px;top:170px;width:223px;height:44px;font-size:28px">e-book</div>
  <ul class="topics" style="left:50px;top:412px;font-size:28px">
    <li class="lead">Alles über</li><li>Maut- &amp; Tunnelgebühren</li><li>Campingplätze</li><li>Sehenswürdigkeiten</li>
  </ul>
  <div class="book" style="left:143px;top:548px;width:207px;height:370px">
    <div class="book-title" style="font-size:34px">Unterwegs<br>im Süden<br>Ungarns<span class="book-sub" style="font-size:13px">Der perfekte Guide für Fahrer &amp; Beifahrer</span></div>
    <div class="book-seal" style="width:50px;height:50px"></div>
    <div class="book-art" role="img" aria-label="Coverfoto einer Altstadt am Meer"></div>
    <div class="book-author" style="font-size:13px">Lena Vostrik</div>
  </div>
</section>

<section class="banner ad-wide" aria-label="Banner 728 x 90">
  <div class="photo photo-wide" role="img" aria-label="Luftbild von Inseln an der Küste"></div>
  <h2 class="shout" style="left:233px;top:10px;font-size:46px">
    <span class="line" style="font-size:20px">Unterwegs</span>
    <span class="line">Im <span class="mid">Süden</span></span>
    <span class="line">Ungarns</span>
  </h2>
  <ul class="topics" style="left:537px;top:6px;font-size:20px">
    <li class="lead">Alles über</li><li>Mautgebühren</li><li>Tunnelgebühren</li><li>Campingplätze</li><li>Sehenswürdigkeiten</li>
  </ul>
  <div class="tab-red" style="left:769px;top:3px;width:243px;height:62px;font-size:20px;padding-top:5px">Der perfekte Guide<br>für Fahrer &amp; Beifahrer</div>
  <div class="tab-ebook" style="left:832px;top:85px;width:180px;height:42px;font-size:26px">e-book</div>
  <div class="book" style="left:1012px;top:5px;width:105px;height:134px">
    <div class="book-title" style="font-size:14px">Unterwegs<br>im Süden<br>Ungarns</div>
    <div class="book-seal" style="width:20px;height:20px"></div>
    <div class="book-art" role="img" aria-label="Coverfoto einer Altstadt am Meer"></div>
    <div class="book-author" style="font-size:7px">Lena Vostrik</div>
  </div>
</section>

</body>
</html>
```